Design the Business card for VaultPeak

Business card required for a professional Cyber Security business.
Company Logo and Icon has already been provided however I would like other options for the logo and icon to compare to. Alternatively, please refine/enhance the image of the logo.icon I have already provided.

If you are going to use the provided logo and icon, I was thinking that the company raised Logo on White background would serve well on the front of the card. See attached. AND, a large company raised stand-alone icon to appear on black background on the back of the card with tagline 'Cyber Risk Management, Governance and Consulting' or 'Cyber Security for your Business' See attached.
Alternatively, provide your own design for the logo and icon.

Target Market(s)

Enterprise, Government, Financial.

Contact Information for Business Card

Teodor Halvik
Founder and CEO

Email Address
Mobile Number
Website URL
LinkedIn URL

Logo Text

VaultPeak - see attached example of logo

Font styles to use
Other font styles liked:
• Berlin Sans FB

Requirements
Must have
• Clean large and bold icon on the back with tagline.
• Horizontal alignment,
Nice to have
• Round edges.
• Raised Logo/Icon
Should not have
• An unprofessional look and feel.

```html
<!DOCTYPE html>
<html lang="en">
<head>
<meta charset="utf-8">
<title>VaultPeak Business Card</title>
<link rel="stylesheet" href="https://fonts.googleapis.com/css2?family=Arimo:wght@400;700&family=Lato:wght@400;700&display=swap">
<style>
  :root {
    --backdrop: #d9d9d9;
    --card-white: #f4f4f4;
    --card-black: #000000;
    --brand-blue: #3f6cc4;
    --brand-yellow: #f7c12a;
    --ink: #222222;
    --rule: #555555;
    --tagline: #ffffff;
  }
  * { margin: 0; padding: 0; box-sizing: border-box; }
  html, body { width: 1200px; height: 1200px; overflow: hidden; }
  body { background: var(--backdrop); position: relative; font-family: "Arimo", Arial, sans-serif; }

  .card { position: absolute; border-radius: 18px; }
  .card-front { left: 234px; top: 311px; width: 363px; height: 593px; background: var(--card-white); }
  .card-back { left: 628px; top: 312px; width: 367px; height: 592px; background: var(--card-black); }

  .wordmark { position: absolute; left: 0; right: 0; display: flex; align-items: center; justify-content: center; gap: 12px; color: var(--brand-blue); font-family: "Arimo", Arial, sans-serif; font-weight: 700; }
  .wordmark-dot { border-radius: 50%; background: var(--brand-blue); flex: none; }
  .card-front .wordmark { top: 140px; font-size: 40px; }
  .card-front .wordmark-dot { width: 56px; height: 56px; }
  .card-back .wordmark { top: 250px; flex-direction: column; gap: 18px; font-family: "Lato", sans-serif; font-size: 40px; }
  .card-back .wordmark-dot { width: 130px; height: 130px; }

  .person-name { position: absolute; top: 350px; left: 0; right: 0; text-align: center; font-size: 23px; font-weight: 700; letter-spacing: 0.2px; }
  .person-name .first { color: var(--brand-blue); }
  .person-name .last { color: var(--brand-yellow); }
  .person-role { position: absolute; top: 378px; left: 0; right: 0; text-align: center; font-size: 18px; color: var(--ink); }

  .contact-icons { position: absolute; top: 424px; left: 77px; width: 224px; display: flex; align-items: center; gap: 4px; }
  .contact-icons .rule { flex: 1; height: 1px; background: var(--rule); }
  .contact-icons svg { width: 24px; height: 24px; display: block; }

  .contact-list { position: absolute; top: 460px; left: 0; right: 0; text-align: center; list-style: none; font-size: 17px; line-height: 21.7px; color: var(--ink); }

  .tagline { position: absolute; top: 488px; left: 0; right: 0; text-align: center; font-family: "Lato", sans-serif; font-size: 15px; line-height: 24px; color: var(--tagline); text-transform: uppercase; }
</style>
</head>
<body>
  <section class="card card-front">
    <div class="wordmark"><span class="wordmark-dot"></span><span>VaultPeak</span></div>
    <p class="person-name"><span class="first">TEODOR</span> <span class="last">HALVIK</span></p>
    <p class="person-role">Founder and CEO</p>
    <div class="contact-icons">
      <span class="rule"></span>
      <svg viewBox="0 0 24 24" aria-label="Phone"><circle cx="12" cy="12" r="12" fill="var(--brand-blue)"/><path d="M6 10c0-2 3-3 6-3s6 1 6 3l-2 1-1-2h-6l-1 2zM8 12h8l1 5H7z" fill="#fff"/></svg>
      <svg viewBox="0 0 24 24" aria-label="Email"><circle cx="12" cy="12" r="12" fill="var(--brand-blue)"/><rect x="6" y="8" width="12" height="8" fill="#fff"/><path d="M6 8l6 5 6-5" fill="none" stroke="var(--brand-blue)" stroke-width="1.2"/></svg>
      <svg viewBox="0 0 24 24" aria-label="Website"><circle cx="12" cy="12" r="12" fill="var(--brand-blue)"/><circle cx="12" cy="12" r="6" fill="none" stroke="#fff" stroke-width="1.5"/><path d="M6 12h12M12 6c-3 3-3 9 0 12M12 6c3 3 3 9 0 12" fill="none" stroke="#fff" stroke-width="1.2"/></svg>
      <svg viewBox="0 0 24 24" aria-label="Professional profile"><circle cx="12" cy="12" r="12" fill="var(--brand-blue)"/></svg>
      <span class="rule"></span>
    </div>
    <ul class="contact-list">
      <li>044-987 654 321</li>
      <li>hello@vaultpeak.com</li>
      <li>www.vaultpeak.com</li>
      <li>in/teodorhalvik</li>
    </ul>
  </section>

  <section class="card card-back">
    <div class="wordmark"><span class="wordmark-dot"></span><span>VaultPeak</span></div>
    <p class="tagline">Cyber Risk Management<br>Governance and Consulting</p>
  </section>
</body>
</html>
```